Postcard Design

Vantora Systems is the single source which provides audio visual technology solutions. we will undoubtedly save you time and will cut Audio visual cost dramatically. We provide the technology for your Large scale meetings, Events, Trade shows, product launches Pharma roll-outs nationwide. we customize online order form to customize your needs and save you time.

our motto; Raising the standards in service to our clients

Industry/Entity Type

Trade

```html
<!DOCTYPE html>
<html lang="en">
<head>
<meta charset="utf-8">
<title>Vantora Systems Postcard</title>
<link rel="stylesheet" href="https://fonts.googleapis.com/css2?family=Cormorant+Garamond:wght@400;700&display=swap">
<style>
  :root {
    --backdrop: #e9e6e2;
    --card-white: #ffffff;
    --photo-deep: #0f3a4a;
    --photo-teal: #2f8f95;
    --photo-green: #58b28a;
    --photo-light: #9ed3cf;
    --text-light: #ffffff;
    --brand-dark: #2a2a2a;
    --rule-grey: #c9c9c9;
    --divider-grey: #8f8f8f;
    --stamp-line: #333333;
    --serif: "Cormorant Garamond", Georgia, serif;
  }
  * { box-sizing: border-box; margin: 0; padding: 0; }
  html, body {
    width: 1200px;
    height: 857px;
    overflow: hidden;
    background: var(--backdrop);
    font-family: var(--serif);
  }
  .canvas {
    position: relative;
    width: 1200px;
    height: 857px;
  }
  .postcard {
    position: absolute;
    width: 466px;
    height: 361px;
    box-shadow: 0 6px 14px rgba(0,0,0,0.25);
  }
  .postcard--front { left: 120px; top: 199px; overflow: hidden; }
  .postcard--back { left: 607px; top: 312px; background: var(--card-white); }

  .front-photo {
    position: absolute;
    inset: 0;
    background:
      radial-gradient(ellipse at 30% 70%, var(--photo-light) 0%, transparent 45%),
      linear-gradient(160deg, var(--photo-deep) 0%, var(--photo-teal) 45%, var(--photo-green) 75%, var(--photo-deep) 100%);
  }
  .motto {
    position: absolute;
    left: 34px;
    top: 52px;
    color: var(--text-light);
    font-size: 19px;
    line-height: 22px;
    text-shadow: 0 1px 3px rgba(0,0,0,0.5);
  }
  .motto__lead { font-weight: 400; }
  .motto__emphasis { display: block; padding-left: 37px; font-weight: 700; }

  .brand {
    position: absolute;
    display: flex;
    align-items: center;
    gap: 8px;
    font-family: var(--serif);
    font-weight: 700;
    font-size: 22px;
    line-height: 1;
  }
  .brand__mark { width: 12px; height: 12px; flex: none; }
  .brand--front { right: 14px; top: 60px; color: var(--text-light); }
  .brand--front .brand__mark { background: var(--text-light); }
  .brand--back { left: 21px; top: 56px; color: var(--brand-dark); font-size: 19px; }
  .brand--back .brand__mark { background: var(--brand-dark); }

  .divider {
    position: absolute;
    left: 220px;
    top: 64px;
    width: 1px;
    height: 248px;
    background: var(--divider-grey);
  }
  .stamp-box {
    position: absolute;
    left: 382px;
    top: 32px;
    width: 65px;
    height: 79px;
    border: 1.5px solid var(--stamp-line);
  }
  .address-lines {
    position: absolute;
    left: 234px;
    top: 173px;
    width: 213px;
    list-style: none;
  }
  .address-lines li {
    height: 28px;
    border-top: 1px solid var(--rule-grey);
  }
</style>
</head>
<body>
<main class="canvas">
  <section class="postcard postcard--front">
    <div class="front-photo" role="img" aria-label="Close-up photograph of audio mixing console faders in teal and green light"></div>
    <p class="motto">
      <span class="motto__lead">Raising the standards</span>
      <span class="motto__emphasis">in service to our clients</span>
    </p>
    <div class="brand brand--front"><span class="brand__mark"></span>Vantora Systems</div>
  </section>

  <section class="postcard postcard--back">
    <div class="brand brand--back"><span class="brand__mark"></span>Vantora Systems</div>
    <div class="divider"></div>
    <div class="stamp-box"></div>
    <ul class="address-lines">
      <li></li><li></li><li></li><li></li><li></li>
    </ul>
  </section>
</main>
</body>
</html>
```